Crestline Slate & Tile Needs a Business Card

Attached you will find your logo, my photo and design guidelines for a new business card. The final design will need two separate files to create an embossed card. The cards will be printed by www.plinkprint.com (Instructions below)
Format is the Zib SQUARE card
Crestline Slate And Tile is a brick and mortar, retail stone and tile shop.
One the front:
Crestline Slate And Tile
Gerald Finchcombe
Owner
48207 Vesper Hollow Blvd
Suite R & T
Charlotte, NC 28953
Cell: 704-555-0183
Web: www.CrestlineSlateAndTile.com
(Make each word of the domain a different or alternating color)
On the back;
Something that shows beautiful colorful tile
Follow the design guide closely please. For more information see this page that describes creating the spot gloss file: https://www.plinkprint.com/us/business-cards/design-guidelines-spot-gloss
The logo is what we would like to have raised spot glossed.
Format is the Zib SQUARE card. See attahced guidlines.

```html
<!DOCTYPE html>
<html lang="en">
<head>
<meta charset="utf-8">
<title>Crestline Slate &amp; Tile — Business Card</title>
<link rel="stylesheet" href="https://fonts.googleapis.com/css2?family=Marcellus&family=Josefin+Sans:wght@300;400&display=swap">
<style>
  :root{
    --backdrop:#24353d;
    --paper:#fcfbf9;
    --navy:#1f2f3a;
    --rust:#a3452b;
    --gold:#a87436;
    --taupe:#6e6a5c;
    --tile-tan:#d8c6a2;
    --tile-blue:#3f5e78;
    --tile-green:#5c7055;
    --tile-rust:#b55a33;
  }
  *{box-sizing:border-box;margin:0;padding:0}
  html,body{width:1020px;height:1200px;overflow:hidden;background:var(--backdrop)}
  .canvas{position:relative;width:1020px;height:1200px}
  .card{position:absolute;left:53px;width:915px;height:511px}
  .card--front{top:76px}
  .card--back{top:612px;background:var(--paper)}
  .tile-fill{background:linear-gradient(135deg,var(--tile-tan) 0%,var(--tile-blue) 30%,var(--tile-green) 50%,var(--tile-rust) 70%,var(--tile-tan) 100%)}
  .front-border{position:absolute;inset:0}
  .front-panel{position:absolute;left:11px;top:11px;right:11px;bottom:11px;background:var(--paper)}
  .portrait-frame{position:absolute;left:57px;top:53px;width:203px;height:212px;border:2px solid var(--rust)}
  .portrait{position:absolute;left:10px;top:10px;right:10px;bottom:10px;background:linear-gradient(160deg,#4a4b4f,#2c2d31 55%,#b98a6e)}
  .name{position:absolute;left:292px;top:98px;font-family:'Marcellus',serif;font-size:45px;letter-spacing:3px;color:var(--navy);white-space:nowrap;line-height:1}
  .rule{position:absolute;height:1px;background:var(--gold)}
  .diamond{position:absolute;width:11px;height:11px;background:var(--gold);transform:rotate(45deg)}
  .title{position:absolute;left:300px;top:196px;font-family:'Josefin Sans',sans-serif;font-weight:300;font-size:27px;letter-spacing:19px;color:var(--rust);line-height:1}
  .contact{position:absolute;font-family:'Marcellus',serif;font-size:21px;color:var(--navy);line-height:1;white-space:nowrap;letter-spacing:.5px}
  .contact .muted{color:var(--taupe)}
  .contact .accent{color:var(--rust)}
  .divider{position:absolute;left:417px;top:352px;width:1px;height:78px;background:var(--gold)}
  .icon{position:absolute;width:24px;height:24px}
  .back-tiles{position:absolute;left:0;top:0;width:915px;height:511px}
  .back-tiles--left{clip-path:polygon(11px 11px,257px 11px,257px 125px,147px 238px,257px 347px,257px 469px,370px 469px,401px 500px,11px 500px)}
  .back-tiles--right{clip-path:polygon(904px 11px,658px 11px,658px 125px,768px 238px,658px 347px,658px 469px,545px 469px,514px 500px,904px 500px)}
  .brand-mark{position:absolute;left:450px;top:176px;width:16px;height:16px;background:var(--navy)}
  .brand-name{position:absolute;left:0;width:915px;text-align:center;font-family:'Marcellus',serif;color:var(--navy);line-height:1;white-space:nowrap}
  .brand-name--main{top:250px;font-size:56px;letter-spacing:10px}
  .brand-name--sub{top:328px;font-size:24px;letter-spacing:12px}
</style>
</head>
<body>
<main class="canvas">
  <section class="card card--front">
    <div class="front-border tile-fill" role="img" aria-label="Colorful geometric tile pattern border"></div>
    <div class="front-panel">
      <div class="portrait-frame">
        <div class="portrait" role="img" aria-label="Portrait photo of Gerald Finchcombe"></div>
      </div>
      <h1 class="name">GERALD FINCHCOMBE</h1>
      <div class="rule" style="left:299px;top:172px;width:240px"></div>
      <div class="diamond" style="left:549px;top:167px"></div>
      <div class="rule" style="left:568px;top:172px;width:240px"></div>
      <p class="title">OWNER</p>

      <svg class="icon" style="left:87px;top:347px" viewBox="0 0 24 24" fill="none" stroke="#a87436" stroke-width="1.5"><path d="M12 22s7-7 7-12a7 7 0 0 0-14 0c0 5 7 12 7 12z"/><circle cx="12" cy="10" r="2" fill="#a87436"/></svg>
      <p class="contact muted" style="left:111px;top:348px"><span class="muted">48207 Vesper</span> <span style="color:var(--navy)">Hollow Blvd</span></p>
      <p class="contact" style="left:111px;top:385px">Suite R &amp; T</p>
      <p class="contact" style="left:111px;top:422px"><span class="muted">Charlotte,</span> NC <span class="accent">28953</span></p>

      <div class="divider"></div>

      <svg class="icon" style="left:433px;top:352px" viewBox="0 0 24 24" fill="none" stroke="#a87436" stroke-width="1.4"><path d="M5 3l4 1 1 4-2 2a12 12 0 0 0 6 6l2-2 4 1 1 4-2 2C10 21 3 14 3 5z"/></svg>
      <p class="contact" style="left:476px;top:354px">Cell:&nbsp; <span class="accent">704-555-0183</span></p>

      <svg class="icon" style="left:433px;top:399px" viewBox="0 0 24 24" fill="none" stroke="#a87436" stroke-width="1.4"><circle cx="12" cy="12" r="10"/><ellipse cx="12" cy="12" rx="4.5" ry="10"/><path d="M2 12h20M4 7h16M4 17h16"/></svg>
      <p class="contact" style="left:476px;top:402px">Web: www.<span class="accent">Crestline</span>Slate<span class="accent">And</span>Tile.com</p>

      <div class="rule" style="left:120px;top:465px;width:314px"></div>
      <div class="diamond" style="left:440px;top:460px"></div>
      <div class="rule" style="left:467px;top:465px;width:314px"></div>
    </div>
  </section>

  <section class="card card--back">
    <div class="back-tiles back-tiles--left tile-fill" role="img" aria-label="Colorful mosaic tile pattern"></div>
    <div class="back-tiles back-tiles--right tile-fill" role="img" aria-label="Colorful mosaic tile pattern"></div>
    <div class="brand-mark"></div>
    <p class="brand-name brand-name--main">CRESTLINE</p>
    <p class="brand-name brand-name--sub">SLATE &amp; TILE</p>
  </section>
</main>
</body>
</html>
```